Business card design for Automotive workshop

We need a business card for a new automotive repair and tyre shop called Ridgeback Prime Automotive located in New Zealand. We are a clean, modern and fresh workshop and company.

Front needs to feature logo,
my name:
Lachie Westergaard (director)

Address:
48 Marlow Lane
Harrowvale 3584

Phone: 07 842 1937
Mobile: 027 519 2764
Email: office@ridgebackmotors.co.nz
Website: ridgebackmotors.co.nz

Back needs to feature an area to write down appointment details, date and time.

Also feature a list of jobs and work we do such as,
Vehicle Servicing
All Mechanical Repairs
Warrant of Fitness
Tyres & Wheel Alignments
Automotive Diagnostics
Automotive Parts & Supplies

```html
<!DOCTYPE html>
<html lang="en">
<head>
<meta charset="utf-8">
<title>Ridgeback Prime Automotive – Business Card</title>
<link rel="stylesheet" href="https://fonts.googleapis.com/css2?family=Arimo:wght@400&family=Lato:wght@400;700&display=swap">
<style>
  :root {
    --red: #e31e24;
    --black: #0d0d0d;
    --ink: #1c1c1c;
    --paper: #ffffff;
    --backdrop: #ecebe8;
  }
  * { box-sizing: border-box; margin: 0; padding: 0; }
  html, body {
    width: 1200px; height: 1200px; overflow: hidden;
    background: var(--backdrop);
    font-family: "Lato", sans-serif;
    color: var(--ink);
  }
  .card {
    position: absolute;
    width: 824px; height: 474px;
    background: var(--paper);
    box-shadow: 0 4px 14px rgba(0,0,0,0.18);
    overflow: hidden;
  }
  .card--front { left: 188px; top: 83px; }
  .card--back  { left: 186px; top: 643px; width: 829px; }

  .brand-name {
    position: absolute;
    color: var(--red);
    font-weight: 700;
    text-transform: uppercase;
    letter-spacing: 1px;
    line-height: 1.05;
  }
  .card--front .brand-name { left: 48px; top: 203px; width: 330px; font-size: 34px; }
  .card--back .brand-name  { left: 60px; top: 84px;  width: 390px; font-size: 38px; }

  .divider {
    position: absolute; left: 413px; top: 132px;
    width: 2px; height: 214px; background: var(--red);
  }
  .person { position: absolute; left: 456px; top: 124px; }
  .person__name { color: var(--red); font-weight: 700; font-size: 30px; line-height: 1.2; }
  .person__role { font-size: 19px; margin-top: 4px; }

  .contacts { position: absolute; left: 456px; top: 206px; list-style: none; }
  .contacts li {
    display: flex; align-items: center;
    height: 30px; font-size: 20px;
  }
  .contacts svg { width: 20px; height: 20px; margin-right: 9px; flex: none; }

  .front-band { position: absolute; left: 0; bottom: 0; width: 824px; height: 22px; }

  .services {
    position: absolute; left: 510px; top: 36px; list-style: none;
    font-family: "Arimo", sans-serif;
  }
  .services li {
    position: relative; padding-left: 16px;
    font-size: 19px; height: 28px; line-height: 28px;
  }
  .services li::before {
    content: ""; position: absolute; left: 0; top: 11px;
    width: 7px; height: 7px; border-radius: 50%; background: var(--red);
  }

  .appointment { position: absolute; left: 60px; top: 222px; width: 708px; }
  .appointment__title { color: var(--red); font-weight: 700; font-size: 26px; margin-bottom: 28px; }
  .field-row { display: flex; align-items: baseline; font-size: 22px; height: 44px; }
  .field-row .fill {
    flex: 1; border-bottom: 2px dotted var(--ink);
    margin: 0 4px; transform: translateY(-4px);
  }
  .field-row .fill--time { flex: 0 0 200px; }
  .check { display: inline-flex; align-items: center; margin-right: 10px; }
  .box {
    display: inline-block; width: 16px; height: 16px;
    border: 2px solid var(--ink); margin-right: 4px;
  }
  .days { display: flex; justify-content: space-between; font-size: 20px; margin-top: 2px; }
  .days .check:last-child { margin-right: 0; }
  .days .box { margin-right: 8px; }

  .notice {
    position: absolute; left: 0; bottom: 0; width: 100%; height: 51px;
    background: var(--red); color: var(--paper);
    font-size: 21px; line-height: 51px; text-align: center;
  }
</style>
</head>
<body>

<section class="card card--front">
  <div class="brand-name">Ridgeback Prime<br>Automotive</div>
  <div class="divider"></div>
  <div class="person">
    <div class="person__name">Lachie Westergaard</div>
    <div class="person__role">Director</div>
  </div>
  <ul class="contacts">
    <li>
      <svg viewBox="0 0 20 20"><path d="M10 1.5a6 6 0 0 0-6 6c0 4.5 6 11 6 11s6-6.5 6-11a6 6 0 0 0-6-6z" fill="none" stroke="#e31e24" stroke-width="1.8"/><circle cx="10" cy="7.5" r="2.2" fill="none" stroke="#e31e24" stroke-width="1.8"/></svg>
      48 Marlow Lane, Harrowvale 3584
    </li>
    <li>
      <svg viewBox="0 0 20 20"><path d="M5 2l3 3.5-1.8 2.3c1 2.3 2.7 4 5 5L13.5 11l3.5 3-1.8 3c-6.5-.4-11.5-5.5-12-12z" fill="#e31e24"/></svg>
      07 842 1937
    </li>
    <li>
      <svg viewBox="0 0 20 20"><rect x="5" y="1.5" width="10" height="17" rx="1.5" fill="none" stroke="#e31e24" stroke-width="1.8"/><line x1="9" y1="15.5" x2="11" y2="15.5" stroke="#e31e24" stroke-width="1.6"/></svg>
      027 519 2764
    </li>
    <li>
      <svg viewBox="0 0 20 20"><rect x="2" y="5" width="16" height="11" fill="#e31e24"/><path d="M2 5l8 6 8-6M2 16l6-5M18 16l-6-5" fill="none" stroke="#fff" stroke-width="1.3"/></svg>
      office@ridgebackmotors.co.nz
    </li>
    <li>
      <svg viewBox="0 0 20 20" fill="none" stroke="#e31e24" stroke-width="1.4"><circle cx="10" cy="10" r="8"/><ellipse cx="10" cy="10" rx="3.5" ry="8"/><line x1="2" y1="10" x2="18" y2="10"/><line x1="3" y1="6" x2="17" y2="6"/><line x1="3" y1="14" x2="17" y2="14"/></svg>
      ridgebackmotors.co.nz
    </li>
  </ul>
  <svg class="front-band" viewBox="0 0 824 22" preserveAspectRatio="none">
    <polygon points="0,0 412,0 390,22 0,22" fill="#0d0d0d"/>
    <polygon points="421,0 824,0 824,22 399,22" fill="#e31e24"/>
  </svg>
</section>

<section class="card card--back">
  <div class="brand-name">Ridgeback Prime<br>Automotive</div>
  <ul class="services">
    <li>Vehicle Servicing</li>
    <li>All Mechanical Repairs</li>
    <li>Warrant of Fitness</li>
    <li>Tyres &amp; Wheel Alignments</li>
    <li>Automotive Diagnostics</li>
    <li>Automotive Parts &amp; Supplies</li>
  </ul>
  <div class="appointment">
    <div class="appointment__title">APPOINTMENT</div>
    <div class="field-row">Name:<span class="fill"></span></div>
    <div class="field-row">
      Time:<span class="fill fill--time"></span>
      <span class="check"><span class="box"></span>AM</span>
      <span class="check"><span class="box"></span>PM</span>
      &nbsp;Date:<span class="fill"></span>
    </div>
    <div class="days">
      <span class="check"><span class="box"></span>MON</span>
      <span class="check"><span class="box"></span>TUES</span>
      <span class="check"><span class="box"></span>WED</span>
      <span class="check"><span class="box"></span>THUR</span>
      <span class="check"><span class="box"></span>FRI</span>
      <span class="check"><span class="box"></span>SAT</span>
    </div>
  </div>
  <div class="notice">If you are unable to keep your appointment, please call us within 24 hours.</div>
</section>

</body>
</html>
```